Brochure Design for cool security products

Hello there,
We need a brochure design template for our company wavecrates dot com.
This particular Brochure will be used for download / online distribution but may also be used for printing.
Initially we need a brochure for a particular customer segment (Prisons and Corrections)
We want this to be visually very striking as it needs to sell the concept to the customer.
It really only needs to have about 3 pages total… A very inviting cover page, and 2 inside pages.
We will want you to add in a how it works illustration (so readers have a visual overview of how the solution is installed in their facility)
We plan on using the template design for more brochures also. (for example product sheets and other sectors)
In terms of images we can provide some, however any assistance, inclusion of image work to complement the brochure would be great.
Of course any assistance with real content is greatly appreciated, but if the brochure is supplied in an editable format we can update place holder content ourselves.
Security

```html
<!DOCTYPE html>
<html lang="en">
<head>
<meta charset="utf-8">
<title>Wavecrates Brochure</title>
<link rel="stylesheet" href="https://fonts.googleapis.com/css2?family=Exo+2:wght@500&family=Source+Sans+3:wght@300;400;600&display=swap">
<style>
  :root {
    --backdrop: #8f9195;
    --backdrop-light: #b7b8bb;
    --navy-deep: #101b33;
    --navy: #1f3556;
    --steel: #4d6d92;
    --slate: #5d6c8c;
    --cloud: #ffffff;
    --cloud-shade: #dfe4ec;
    --sky-blue: #4aa3d8;
    --ink-grey: #8a8f98;
    --text-light: #e8eef6;
  }
  * { margin: 0; padding: 0; box-sizing: border-box; }
  html, body { width: 1200px; height: 800px; overflow: hidden; }
  body {
    background: radial-gradient(ellipse at 50% 40%, var(--backdrop-light), var(--backdrop));
    font-family: "Source Sans 3", Arial, sans-serif;
  }
  .spread {
    position: absolute;
    left: 225px; top: 30px;
    width: 750px; height: 740px;
    display: flex;
    box-shadow: 0 18px 40px rgba(0,0,0,.35);
  }
  .page { position: relative; width: 375px; height: 740px; overflow: hidden; }

  /* Cover */
  .cover {
    background: linear-gradient(160deg, var(--steel) 0%, var(--navy) 40%, var(--navy-deep) 75%);
  }
  .cover-visual {
    position: absolute; top: 0; right: 0;
    width: 230px; height: 170px;
    background: radial-gradient(circle at 60% 55%, #3c79c9 0%, #16305e 35%, #060a16 75%);
  }
  .cover-sky-top {
    position: absolute; top: 0; left: 0;
    width: 145px; height: 130px;
    background: linear-gradient(180deg, var(--cloud) 60%, var(--cloud-shade) 100%);
  }
  .brand {
    position: absolute; left: 40px; top: 330px;
    display: flex; align-items: center; gap: 14px;
    font-family: "Exo 2", Arial, sans-serif; font-weight: 500;
    font-size: 38px; letter-spacing: 2px; color: var(--cloud);
  }
  .brand-dot { width: 22px; height: 22px; border-radius: 50%; background: var(--sky-blue); }
  .cover-sky-bottom {
    position: absolute; left: 0; bottom: 0;
    width: 375px; height: 280px;
    background: linear-gradient(180deg, var(--cloud-shade) 0%, var(--cloud) 18%, var(--cloud) 100%);
  }
  .contact { position: absolute; left: 45px; bottom: 95px; }
  .contact-title { font-size: 30px; font-weight: 400; color: var(--sky-blue); margin-bottom: 12px; }
  .contact-line { font-size: 17px; font-weight: 600; color: var(--ink-grey); line-height: 1.15; }

  /* Inside page */
  .about {
    background: linear-gradient(180deg, var(--navy) 0%, var(--slate) 70%, #7d8aa6 100%);
  }
  .about-visual {
    position: absolute; top: 0; left: 0;
    width: 375px; height: 330px;
    background: radial-gradient(circle at 55% 55%, #3a7dc4 0%, #173866 30%, #08101f 70%);
    clip-path: path("M0 0 H375 V250 C330 250 300 270 270 300 C240 330 200 335 150 330 C90 325 40 330 0 345 Z");
  }
  .about-title {
    position: absolute; left: 40px; top: 355px;
    font-size: 26px; font-weight: 300; color: var(--text-light); letter-spacing: .5px;
  }
  .about-body {
    position: absolute; left: 40px; top: 405px; width: 300px;
    font-size: 12.5px; font-weight: 400; line-height: 1.6; color: var(--text-light);
  }
  .about-sky {
    position: absolute; right: 0; bottom: 0;
    width: 220px; height: 90px;
    background: linear-gradient(180deg, var(--cloud-shade) 0%, var(--cloud) 40%);
  }
</style>
</head>
<body>
  <main class="spread">
    <section class="page cover">
      <div class="cover-visual" role="img" aria-label="Illustration of a security operator surrounded by radio signal rings"></div>
      <div class="cover-sky-top" role="img" aria-label="Decorative white cloud illustration"></div>
      <div class="brand"><span>WAVECRATES</span><span class="brand-dot"></span></div>
      <div class="cover-sky-bottom" role="img" aria-label="Decorative white cloud illustration"></div>
      <div class="contact">
        <h2 class="contact-title">Contact</h2>
        <p class="contact-line">USA Toll Free:800-555-0142</p>
        <p class="contact-line">Outside USA:+1-555-010-2864</p>
        <p class="contact-line">USA Fax:555-0107193</p>
      </div>
    </section>

    <section class="page about">
      <div class="about-visual" role="img" aria-label="Illustration of a mobile phone above a glowing blue maze with a signal monitoring dashboard"></div>
      <h2 class="about-title">ABOUT US</h2>
      <p class="about-body">Wavecrates is a leading developer of RF detection and signal source locating technology. Established in 1999, Wavecrates was one of the first companies to address the need to detect, monitor, control and locate cell phone and radio frequency activity. Over the years, cellular technology has changed rapidly, and with reports of over six billion cell phones in use throughout the world, the risks to the security of assets, facilities, information and people as a result of cell phones are now greater than ever.</p>
      <div class="about-sky" role="img" aria-label="Decorative white cloud illustration"></div>
    </section>
  </main>
</body>
</html>
```